Stationery Design needed for logo design project

This company needs a letterhead and envelope for their new practice. We did not want to release this contact until the business card design was finalized so the stationary can be created to coordinate with it.

For those of you that will be submitting designs for this content, think "linear". Designs with curves or "swooshes" are not appropriate for this design.

NOTE: As part of the source files; I will require FULLY LAYERED PHOTOSHOP FILES of all elements, including design elements, text and fonts. If you cannot provide a fully layered PSD file, please do not submit.
Updates

The project details have been updated. We have added a new description along with logo files and business card design. Please review the style of the logo and business card before submitting designs. Thanks

Target Market(s)

Medical

Industry/Entity Type

Business

Requirements
Must have
• NOTE: As part of the source files; I will require FULLY LAYERED PHOTOSHOP FILES of all elements, including design elements, text and fonts. If you cannot provide a fully layered PSD file, please do not submit.

Logo
2 office address locations
phone
fax
email
website URL

```html
<!DOCTYPE html>
<html lang="en">
<head>
<meta charset="utf-8">
<title>Halden &amp; Associates Letterhead</title>
<link href="https://fonts.googleapis.com/css2?family=Cinzel:wght@400&family=Open+Sans:wght@400;600&display=swap" rel="stylesheet">
<style>
  :root {
    --backdrop: #d9d9d9;
    --paper: #ffffff;
    --ink: #1d1d1d;
    --accent: #a61d24;
    --muted: #4a4a4a;
    --watermark: #f1f1f1;
  }
  html, body {
    margin: 0;
    width: 1200px;
    height: 1000px;
    overflow: hidden;
    background: var(--backdrop);
  }
  .letterhead {
    position: absolute;
    left: 282px;
    top: 50px;
    width: 636px;
    height: 900px;
    background: var(--paper);
    box-shadow: 0 2px 6px rgba(0,0,0,0.18);
    font-family: "Open Sans", sans-serif;
    color: var(--muted);
  }
  .brand {
    position: absolute;
    left: 44px;
    top: 48px;
    display: flex;
    align-items: center;
    gap: 12px;
  }
  .brand-dot {
    width: 30px;
    height: 30px;
    border-radius: 50%;
    background: var(--ink);
  }
  .brand-name {
    font-family: "Cinzel", serif;
    font-size: 26px;
    line-height: 1;
    color: var(--ink);
    margin: 0;
    font-weight: 400;
  }
  .brand-tagline {
    font-family: "Cinzel", serif;
    font-size: 9.5px;
    letter-spacing: 1.2px;
    color: var(--accent);
    margin: 5px 0 0;
    text-transform: uppercase;
  }
  .watermark {
    position: absolute;
    left: 208px;
    top: 300px;
    width: 220px;
    height: 220px;
    border-radius: 50%;
    background: var(--watermark);
  }
  .footer-mark {
    position: absolute;
    right: 34px;
    bottom: 104px;
    width: 14px;
    height: 14px;
    border-radius: 50%;
    background: var(--ink);
  }
  .contacts {
    position: absolute;
    left: 44px;
    bottom: 36px;
    display: flex;
    gap: 70px;
    font-size: 8.5px;
    line-height: 1.45;
  }
  .office-title {
    color: var(--accent);
    font-weight: 600;
    margin: 0 0 2px;
    font-size: 9px;
  }
  .line {
    display: flex;
    align-items: flex-start;
    gap: 4px;
    margin: 0;
  }
  .line svg { flex: none; margin-top: 2px; }
  .band-dark {
    position: absolute;
    left: 0;
    bottom: 0;
    width: 470px;
    height: 12px;
    background: var(--ink);
  }
  .band-accent {
    position: absolute;
    right: 0;
    bottom: 0;
    width: 160px;
    height: 18px;
    background: var(--accent);
  }
</style>
</head>
<body>
  <main class="letterhead">
    <header class="brand">
      <div class="brand-dot"></div>
      <div>
        <p class="brand-name">Halden &amp; Associates</p>
        <p class="brand-tagline">Cardiology and Wellness</p>
      </div>
    </header>

    <div class="watermark" aria-hidden="true"></div>
    <div class="footer-mark" aria-hidden="true"></div>

    <footer class="contacts">
      <address class="office" style="font-style:normal">
        <p class="office-title">Downtown Office</p>
        <p class="line">
          <svg width="7" height="9" viewBox="0 0 7 9"><path d="M3.5 0A3.5 3.5 0 0 0 0 3.5C0 6 3.5 9 3.5 9S7 6 7 3.5A3.5 3.5 0 0 0 3.5 0z" fill="var(--accent)"/><circle cx="3.5" cy="3.5" r="1.2" fill="#fff"/></svg>
          <span>148 Larkspur Ave, Suite 12<br>Fairhaven, NM 87350</span>
        </p>
        <p class="line">
          <svg width="7" height="7" viewBox="0 0 7 7"><path d="M1 0h1.5l.6 1.8-.9.7a4 4 0 0 0 2.3 2.3l.7-.9L7 4.5V6a1 1 0 0 1-1 1A6 6 0 0 1 0 1a1 1 0 0 1 1-1z" fill="var(--accent)"/></svg>
          <span>(800) 555-0142</span>
        </p>
      </address>

      <address class="office" style="font-style:normal">
        <p class="office-title">West Side Office</p>
        <p class="line">
          <svg width="7" height="9" viewBox="0 0 7 9"><path d="M3.5 0A3.5 3.5 0 0 0 0 3.5C0 6 3.5 9 3.5 9S7 6 7 3.5A3.5 3.5 0 0 0 3.5 0z" fill="var(--accent)"/><circle cx="3.5" cy="3.5" r="1.2" fill="#fff"/></svg>
          <span>920 Mesa Ridge Rd, Suite 305<br>Westbrook, NM 87361</span>
        </p>
        <p class="line">
          <svg width="7" height="7" viewBox="0 0 7 7"><path d="M1 0h1.5l.6 1.8-.9.7a4 4 0 0 0 2.3 2.3l.7-.9L7 4.5V6a1 1 0 0 1-1 1A6 6 0 0 1 0 1a1 1 0 0 1 1-1z" fill="var(--accent)"/></svg>
          <span>(800) 555-0142</span>
        </p>
      </address>

      <address class="office" style="font-style:normal;padding-top:13px">
        <p class="line">
          <svg width="8" height="7" viewBox="0 0 8 7"><rect x="0" y="1" width="8" height="6" rx="1" fill="var(--accent)"/><rect x="2" y="0" width="4" height="2" fill="var(--accent)"/></svg>
          <span>555-0198-27</span>
        </p>
        <p class="line">
          <svg width="8" height="6" viewBox="0 0 8 6"><rect width="8" height="6" rx="0.8" fill="var(--accent)"/><path d="M0.5 0.7L4 3.4 7.5 0.7" stroke="#fff" stroke-width="0.8" fill="none"/></svg>
          <span>care@haldenheart.com</span>
        </p>
        <p class="line">
          <svg width="7" height="7" viewBox="0 0 7 7"><circle cx="3.5" cy="3.5" r="3.5" fill="var(--accent)"/><path d="M0.5 3.5h6M3.5 0.3c-1.5 2-1.5 4.4 0 6.4M3.5 0.3c1.5 2 1.5 4.4 0 6.4" stroke="#fff" stroke-width="0.6" fill="none"/></svg>
          <span>www.haldenheart.com</span>
        </p>
      </address>
    </footer>

    <div class="band-dark" aria-hidden="true"></div>
    <div class="band-accent" aria-hidden="true"></div>
  </main>
</body>
</html>
```